Quarrelsome Ledgers (Podcast)

A simple website that allows users to follow and sign up to our podcast.

"Quarrelsome Ledgers with Tavi and Brem" is a humourous look at economics and entrepreneurship in the world. We interview up and coming kickstarter projects and established entrepreneurs and subject matter experts. It's about practical real life smarts.

We value liberty, intelligence and humour.

The aim of the website is to attract retain and build a list of young people that share our values.

Podcast we enjoy (But not their website as it's to noisy and scattered): http://www.plimcast.example/

Project Deadline Extended
Reason: To allow for sufficient submission- we are aiming to have the podcast up and functional within 7 days and may award the project alot earlier if the right eye catching design presents. We value creativity and your own influence on the design over our own percieved expectations.

We like the simplicity of the following templates - Steady Spinner and RV Troupe

http://vornaskins.example/shop/steady-audio-skins/steady-spinner/

http://skinbazaar.example/item/rvtroupe-audio-group-premium-site-skin/7315024?WT.ac=category_item&WT.seg_1=category_item&WT.z_author=quillmark

The key is that we are chasing something that optimises list signups and social connectivity.
 

Target Market(s)

Gen Y- Young driven intelligent individuals, that seek out information and are or have aspirations to start their own businesses. Our target market loves to laugh.

Industry/Entity Type

Build

Requirements
Must have
• - Podcast Downloads
- Email sign up
- Affiliate Links with Thumbnail Preview
- Social Sharing and Connectivity
Nice to have
• - Sharing pictures/ youtube videos
Should not have
• Excessive amount of content that distract users from the objective of enjoying the podcast and signing up to our list.

```html
<!DOCTYPE html>
<html lang="en">
<head>
<meta charset="utf-8">
<title>Quarrelsome Ledgers with Tavi and Brem</title>
<link rel="stylesheet" href="https://fonts.googleapis.com/css2?family=Open+Sans:wght@300;400;600;700;800&family=Montserrat:wght@700&display=swap">
<style>
:root{
  --red:#d7202a;
  --red-dark:#a8151d;
  --charcoal:#262626;
  --charcoal-deep:#1b1b1b;
  --page:#e4e4e4;
  --white:#ffffff;
  --ink:#555555;
  --ink-soft:#8a8a8a;
  --row:#ececec;
  --row-alt:#f6f6f6;
  --row-active:#e9b1b4;
  --sky:#1e9be8;
  --sponsor:#3a5f8a;
}
*{box-sizing:border-box;margin:0;padding:0}
html,body{width:800px;height:1200px;overflow:hidden}
body{position:relative;background:var(--page);font-family:"Open Sans",Arial,sans-serif;color:var(--ink)}
.abs{position:absolute}

/* navigation */
.site-nav{position:absolute;left:0;top:0;width:800px;height:31px;background:linear-gradient(#e0262f,#b9161f);border-bottom:1px solid #7a0d12}
.nav-item{position:absolute;top:0;height:31px;display:flex;align-items:center;gap:7px;color:var(--white);font-size:9.5px;font-weight:600;padding:0 16px}
.nav-item.is-active{background:var(--red-dark)}
.nav-item svg{width:12px;height:12px;fill:var(--white)}

/* header */
.masthead{position:absolute;left:0;top:31px;width:800px;height:222px;background:radial-gradient(ellipse at 40% 40%,#333 0%,var(--charcoal) 55%,var(--charcoal-deep) 100%)}
.host-art{position:absolute;left:89px;top:25px;width:263px;height:94px;border-radius:6px;background:linear-gradient(90deg,#7d1a1e,#3a3a3a 40%,#4a4a4a 60%,#7d1a1e)}
.brand{position:absolute;left:56px;top:140px;width:320px;text-align:center;color:var(--white);font-family:"Montserrat",Arial,sans-serif;font-weight:700}
.brand-name{font-size:20px;letter-spacing:.5px;line-height:1}
.brand-sub{margin-top:5px;font-size:11px;letter-spacing:1px;display:flex;align-items:center;gap:8px}
.brand-sub::before,.brand-sub::after{content:"";flex:1;height:1px;background:var(--white)}
.next-label{position:absolute;left:425px;top:40px;color:var(--white);font-size:8.5px;font-weight:600}
.next-title{position:absolute;left:424px;top:46px;color:var(--white);font-size:29px;font-weight:800;letter-spacing:-.3px;line-height:36px;white-space:nowrap}
.next-rule{position:absolute;left:425px;top:85px;width:315px;height:1px;background:#777}
.offer{position:absolute;left:428px;top:88px;width:300px;color:#b5b5b5;font-size:11.5px;line-height:14px}
.signup{position:absolute;left:428px;top:126px;width:228px;height:22px;background:#eeeeee;border:1px solid #bbb;display:flex;align-items:center;gap:10px;padding-left:8px;font-size:8px;color:#777;letter-spacing:.3px}
.signup svg{width:14px;height:12px;fill:#888}
.social{position:absolute;top:162px;width:21px;height:21px;border-radius:4px;background:var(--red)}

/* player */
.player{position:absolute;left:58px;top:290px;width:420px;height:233px;background:var(--white);box-shadow:0 1px 4px rgba(0,0,0,.35)}
.cover{position:absolute;left:0;top:0;width:205px;height:207px;background:linear-gradient(160deg,#d9d9d9,#8c7a6a 55%,#3a3a3a)}
.track-head{position:absolute;left:220px;top:6px;width:190px}
.track-title{font-size:11.5px;font-weight:600;color:#444}
.track-date{font-size:7px;color:#666}
.track-actions{position:absolute;right:8px;top:12px;display:flex;gap:8px}
.track-actions svg{width:10px;height:10px;fill:#bbb}
.playlist{position:absolute;left:205px;top:35px;width:215px}
.playlist li{list-style:none;height:22px;display:flex;align-items:center;padding-left:15px;font-size:8.5px;color:#666;background:var(--row-alt)}
.playlist li:nth-child(odd){background:var(--row)}
.playlist li.is-playing{background:var(--row-active)}
.playlist .num{width:14px;font-size:6.5px;color:#999}
.scrollbar{position:absolute;left:413px;top:62px;width:2px;height:118px;background:#bbb}
.controls{position:absolute;left:0;top:207px;width:420px;height:26px;background:#f3f3f3;border-top:1px solid #ddd}
.controls svg{position:absolute;top:8px;height:10px;fill:#666}
.time{position:absolute;top:7px;font-size:7.5px;color:#666}
.progress{position:absolute;left:103px;top:12px;width:193px;height:3px;background:#ccc;border-radius:2px}
.progress-fill{width:146px;height:3px;background:var(--red);border-radius:2px}
.progress-knob{position:absolute;left:142px;top:-3px;width:9px;height:9px;border-radius:50%;background:var(--white);border:2px solid #888}

/* sponsors */
.sponsors-title{position:absolute;left:518px;top:288px;width:222px;text-align:center;font-size:23px;font-weight:400;color:#222;letter-spacing:.5px}
.sponsor{position:absolute;width:112px;text-align:center;color:var(--sponsor);font-weight:700;font-size:13px;line-height:15px;transform:translateX(-50%)}

/* episodes */
.episode{position:absolute;width:201px;height:101px;background:var(--white);box-shadow:0 1px 3px rgba(0,0,0,.35)}
.episode-photo{position:absolute;left:0;top:0;width:100px;height:101px}
.photo-mono{background:linear-gradient(135deg,#c9c9c9,#5e5e5e 60%,#2a2a2a)}
.photo-guest{background:linear-gradient(180deg,#f2f2f2 0%,#e2e2e2 45%,#1f3f7a 60%,#173266 100%)}
.episode-num{position:absolute;left:107px;top:3px;font-size:21px;font-weight:700;color:#555}
.episode-name{position:absolute;left:107px;top:32px;font-size:11.5px;color:var(--red)}
.episode-date{position:absolute;left:107px;top:48px;font-size:5.5px;color:#777;letter-spacing:.2px}

/* tweets */
.tweets{position:absolute;left:518px;top:556px;width:223px;height:367px;background:var(--white);box-shadow:0 1px 3px rgba(0,0,0,.25)}
.tweets-head{height:37px;background:var(--sky);color:var(--white);position:relative}
.tweets-head .bird{position:absolute;left:10px;top:9px;width:19px;height:19px;border-radius:50%;background:var(--white)}
.tweets-head .who{position:absolute;left:40px;top:5px;font-size:12px}
.tweets-head .handle{position:absolute;left:40px;top:20px;font-size:8px;font-weight:700;color:#0c3b66}
.tweet{position:relative;height:54px;border-bottom:1px solid #e4e4e4}
.tweet .avatar{position:absolute;left:7px;top:7px;width:27px;height:27px;background:linear-gradient(#cfe6f5,#2a6fb5)}
.tweet p{position:absolute;left:40px;top:4px;width:160px;font-size:8.2px;line-height:11px;color:#555}
.tweet b{color:#222}
.tweet .ago{position:absolute;right:12px;top:6px;font-size:6.5px;color:#999}

/* footer */
.site-footer{position:absolute;left:0;top:1090px;width:800px;height:110px;background:var(--charcoal);border-top:4px solid #151515}
.footer-links{position:absolute;top:24px;list-style:none;font-size:8.5px;color:var(--white);line-height:14.5px}
.copyright{position:absolute;left:108px;top:85px;font-size:8.5px;color:var(--white)}
.copyright span{color:var(--red)}
.footer-art{position:absolute;left:570px;top:12px;width:125px;height:46px;border-radius:5px;background:linear-gradient(90deg,#6d171b,#3c3c3c 45%,#6d171b)}
.footer-brand{position:absolute;left:548px;top:64px;width:170px;text-align:center;color:var(--white);font-family:"Montserrat",Arial,sans-serif;font-weight:700}
.footer-brand .brand-name{font-size:10.5px}
.footer-brand .brand-sub{font-size:6px;margin-top:2px;gap:4px}
</style>
</head>
<body>

<nav class="site-nav">
  <div class="nav-item is-active" style="left:66px;width:75px"><svg viewBox="0 0 12 12"><path d="M6 1 0 6h2v5h3V8h2v3h3V6h2z"/></svg>Home</div>
  <div class="nav-item" style="left:147px"><svg viewBox="0 0 12 12"><rect x="4" y="0" width="4" height="7" rx="2"/><path d="M2 5h1a3 3 0 0 0 6 0h1a4 4 0 0 1-3.5 4V11h-1V9A4 4 0 0 1 2 5z"/></svg>Live</div>
  <div class="nav-item" style="left:220px"><svg viewBox="0 0 12 12"><path d="M0 1h12v8H5l-3 3V9H0z"/></svg>Ask Questions</div>
  <div class="nav-item" style="left:334px"><svg viewBox="0 0 12 12"><path d="M0 1h2l1 2h9l-1 5H4L2 2H0z"/><circle cx="5" cy="10.5" r="1.2"/><circle cx="10" cy="10.5" r="1.2"/></svg>Downloads</div>
</nav>

<header class="masthead">
  <div class="host-art" role="img" aria-label="Illustration of the two hosts with speech banners"></div>
  <div class="brand">
    <div class="brand-name">QUARRELSOME LEDGERS</div>
    <div class="brand-sub">WITH TAVI AND BREM</div>
  </div>

  <div class="next-label">NEXT EPISODE: OCTOBER 10TH</div>
  <h1 class="next-title">WITH DORRIT VANE</h1>
  <div class="next-rule"></div>
  <p class="offer">Get instant access &amp; Lifetime Membership with our Limited Offer.</p>
  <div class="signup"><svg viewBox="0 0 14 12"><circle cx="5" cy="3" r="3"/><path d="M0 12a5 5 0 0 1 10 0z"/><circle cx="10" cy="3.5" r="2.5"/><path d="M9 7a4 4 0 0 1 5 5h-3a6 6 0 0 0-2-5z"/></svg>EMAIL ADDRESS</div>
  <div class="social" style="left:428px" aria-label="Social link"></div>
  <div class="social" style="left:463px" aria-label="Social link"></div>
  <div class="social" style="left:499px" aria-label="Social link"></div>
  <div class="social" style="left:534px" aria-label="Social link"></div>
  <div class="social" style="left:570px" aria-label="Social link"></div>
</header>

<section class="player">
  <div class="cover" role="img" aria-label="Magazine cover artwork for the current episode"></div>
  <div class="track-head">
    <div class="track-title">20. MARLO PETTIGREW</div>
    <div class="track-date">14TH OCTOBER 2013</div>
  </div>
  <div class="track-actions">
    <svg viewBox="0 0 10 10"><path d="M5 0l1.5 3.2 3.5.4-2.6 2.4.7 3.5L5 7.8 1.9 9.5l.7-3.5L0 3.6l3.5-.4z"/></svg>
    <svg viewBox="0 0 10 10"><path d="M0 3h1v6h8V6h1v4H0zM5 0h5v5L8 3 4 7 3 6l4-4z"/></svg>
  </div>
  <ul class="playlist">
    <li><span class="num">1</span>ODELL BRISK</li>
    <li><span class="num">2</span>FENN HALLOWAY</li>
    <li class="is-playing"><span class="num">3</span>ODELL BRISK</li>
    <li><span class="num">4</span>FENN HALLOWAY</li>
    <li><span class="num">5</span>ODELL BRISK</li>
    <li><span class="num">6</span>FENN HALLOWAY</li>
    <li><span class="num">7</span>ODELL BRISK</li>
  </ul>
  <div class="scrollbar"></div>
  <div class="controls">
    <svg style="left:20px;width:10px" viewBox="0 0 10 10"><path d="M0 0h2v10H0zM10 0v10L5 5zM6 0v10L2 5z"/></svg>
    <svg style="left:43px;width:8px" viewBox="0 0 8 10"><path d="M0 0h3v10H0zM5 0h3v10H5z"/></svg>
    <svg style="left:63px;width:10px" viewBox="0 0 10 10"><path d="M10 0H8v10h2zM0 0v10l5-5zM4 0v10l5-5z"/></svg>
    <span class="time" style="left:84px">4:17</span>
    <div class="progress"><div class="progress-fill"></div><div class="progress-knob"></div></div>
    <span class="time" style="left:300px">5:26</span>
    <svg style="left:332px;width:9px" viewBox="0 0 9 10"><path d="M0 3h3l4-3v10L3 7H0z"/></svg>
    <svg style="left:354px;width:10px" viewBox="0 0 10 10"><path d="M1 0h1v10H1zM4.5 0h1v10h-1zM8 0h1v10H8zM0 6h3v1H0zM3.5 2h3v1h-3zM7 5h3v1H7z"/></svg>
    <svg style="left:378px;width:11px" viewBox="0 0 11 10"><path d="M0 2h3l4 5h2V5.5L11 7.5 9 9.5V8H6.5l-4-5H0zM0 7h2.5l1-1.2.7.9L3 8H0zM6.5 2H9V.5L11 2.5 9 4.5V3H7l-1 1.2-.7-.9z"/></svg>
    <svg style="left:402px;width:10px" viewBox="0 0 10 10"><path d="M5 1a4 4 0 1 0 4 4H8a3 3 0 1 1-3-3v2l3-2.5L5-1z"/></svg>
  </div>
</section>

<h2 class="sponsors-title">SPONSORS</h2>
<div class="sponsor" style="left:577px;top:337px">Corvela</div>
<div class="sponsor" style="left:692px;top:329px">Datamill Works</div>
<div class="sponsor" style="left:577px;top:385px">Emberfox</div>
<div class="sponsor" style="left:692px;top:381px;font-weight:700">Mnemora</div>
<div class="sponsor" style="left:577px;top:420px;font-size:10px">Harlow Link</div>
<div class="sponsor" style="left:692px;top:416px">Kelp</div>
<div class="sponsor" style="left:577px;top:466px">Isoma Partners</div>
<div class="sponsor" style="left:692px;top:466px">Brightsoft</div>

<article class="episode" style="left:58px;top:555px"><div class="episode-photo photo-mono" role="img" aria-label="Black and white guest portrait"></div><div class="episode-num">24</div><div class="episode-name">Rue Tallis</div><div class="episode-date">15TH SEPTEMBER 2013</div></article>
<article class="episode" style="left:277px;top:555px"><div class="episode-photo photo-guest" role="img" aria-label="Guest portrait in blue sweater"></div><div class="episode-num">24</div><div class="episode-name">Rue Tallis</div><div class="episode-date">15TH SEPTEMBER 2013</div></article>
<article class="episode" style="left:60px;top:677px"><div class="episode-photo photo-mono" role="img" aria-label="Black and white guest portrait"></div><div class="episode-num">24</div><div class="episode-name">Rue Tallis</div><div class="episode-date">15TH SEPTEMBER 2013</div></article>
<article class="episode" style="left:279px;top:677px"><div class="episode-photo photo-guest" role="img" aria-label="Guest portrait in blue sweater"></div><div class="episode-num">24</div><div class="episode-name">Rue Tallis</div><div class="episode-date">15TH SEPTEMBER 2013</div></article>
<article class="episode" style="left:58px;top:800px"><div class="episode-photo photo-mono" role="img" aria-label="Black and white guest portrait"></div><div class="episode-num">24</div><div class="episode-name">Rue Tallis</div><div class="episode-date">15TH SEPTEMBER 2013</div></article>
<article class="episode" style="left:277px;top:800px"><div class="episode-photo photo-guest" role="img" aria-label="Guest portrait in blue sweater"></div><div class="episode-num">24</div><div class="episode-name">Rue Tallis</div><div class="episode-date">15TH SEPTEMBER 2013</div></article>
<article class="episode" style="left:60px;top:922px"><div class="episode-photo photo-mono" role="img" aria-label="Black and white guest portrait"></div><div class="episode-num">24</div><div class="episode-name">Rue Tallis</div><div class="episode-date">15TH SEPTEMBER 2013</div></article>
<article class="episode" style="left:279px;top:922px"><div class="episode-photo photo-guest" role="img" aria-label="Guest portrait in blue sweater"></div><div class="episode-num">24</div><div class="episode-name">Rue Tallis</div><div class="episode-date">15TH SEPTEMBER 2013</div></article>

<aside class="tweets">
  <div class="tweets-head"><span class="bird"></span><span class="who">Tavi and Brem</span><span class="handle">@quarrelsomeledgers</span></div>
  <div class="tweet"><div class="avatar" role="img" aria-label="Host avatar"></div><p><b>Brem</b> @quarrelsomeledgers Lorem ipsum dolor sit amet, con sectetur adipiscing elit. Suspendisse consectetur egestaslorem.</p><span class="ago">1h</span></div>
  <div class="tweet"><div class="avatar" role="img" aria-label="Host avatar"></div><p><b>Brem</b> @quarrelsomeledgers Lorem ipsum dolor sit amet, con sectetur adipiscing elit. Suspendisse consectetur egestaslorem.</p><span class="ago">1h</span></div>
  <div class="tweet"><div class="avatar" role="img" aria-label="Host avatar"></div><p><b>Brem</b> @quarrelsomeledgers Lorem ipsum dolor sit amet, con sectetur adipiscing elit. Suspendisse consectetur egestaslorem.</p><span class="ago">1h</span></div>
  <div class="tweet"><div class="avatar" role="img" aria-label="Host avatar"></div><p><b>Brem</b> @quarrelsomeledgers Lorem ipsum dolor sit amet, con sectetur adipiscing elit. Suspendisse consectetur egestaslorem.</p><span class="ago">1h</span></div>
  <div class="tweet"><div class="avatar" role="img" aria-label="Host avatar"></div><p><b>Brem</b> @quarrelsomeledgers Lorem ipsum dolor sit amet, con sectetur adipiscing elit. Suspendisse consectetur egestaslorem.</p><span class="ago">1h</span></div>
  <div class="tweet" style="border-bottom:none"><div class="avatar" role="img" aria-label="Host avatar"></div><p><b>Brem</b> @quarrelsomeledgers Lorem ipsum dolor sit amet, con sectetur adipiscing elit. Suspendisse consectetur egestaslorem.</p><span class="ago">1h</span></div>
</aside>

<footer class="site-footer">
  <ul class="footer-links" style="left:108px"><li>Home</li><li>Podcasts</li><li>Downloads</li></ul>
  <ul class="footer-links" style="left:178px"><li>About us</li><li>Contact us</li></ul>
  <p class="copyright"><span>QUARRELSOME LEDGERS</span> - Copyright 2013 | All Rights Reserved.</p>
  <div class="footer-art" role="img" aria-label="Illustration of the two hosts"></div>
  <div class="footer-brand">
    <div class="brand-name">QUARRELSOME LEDGERS</div>
    <div class="brand-sub">WITH TAVI AND BREM</div>
  </div>
</footer>

</body>
</html>
```